Business Card Design

I am a self-employed qualified carpenter with the business name Tarnwick Joinery. I would like to incorporate the attached logo with a black background with white writing and keep the blue and green that is in my logo if possible.

Industry/Entity Type

Business

Contact Information for Business Card

The attached logo Tarnwick Joinery. Marcus Pelbury, Qualified Carpenter, mobile number 0419 586 274, email marcpelbury@tarnmail.example, postal address PO Box 617 KELVALE VIC 3918, ABN 47 608 924 315.

```html
<!DOCTYPE html>
<html lang="en">
<head>
<meta charset="utf-8">
<title>Tarnwick Joinery – Business Card</title>
<link href="https://fonts.googleapis.com/css2?family=Open+Sans:wght@400&display=swap" rel="stylesheet">
<style>
  :root {
    --backdrop: #6b6c70;
    --silver-light: #ffffff;
    --silver-mid: #e4e5e7;
    --silver-dark: #c9cbce;
    --card-black: #060708;
    --brand-blue: #1a78c2;
    --brand-green: #3aa655;
    --band-light: #3cbcee;
    --band-deep: #3558bd;
    --text-white: #ffffff;
  }
  html, body {
    margin: 0;
    padding: 0;
    width: 1200px;
    height: 820px;
    overflow: hidden;
    background: var(--backdrop);
  }
  .card {
    position: absolute;
    left: 115px;
    top: 144px;
    width: 972px;
    height: 554px;
    overflow: hidden;
    font-family: "Open Sans", Arial, sans-serif;
    background:
      repeating-linear-gradient(180deg, rgba(255,255,255,0.55) 0 2px, rgba(200,202,206,0.35) 2px 3px, rgba(255,255,255,0.2) 3px 6px),
      linear-gradient(160deg, var(--silver-dark) 0%, var(--silver-mid) 35%, var(--silver-light) 75%, var(--silver-mid) 100%);
  }
  .card-shapes {
    position: absolute;
    inset: 0;
    width: 100%;
    height: 100%;
  }
  .brand {
    position: absolute;
    left: 60px;
    top: 206px;
    display: flex;
    align-items: center;
    gap: 18px;
  }
  .brand-mark {
    width: 24px;
    height: 24px;
    background: var(--brand-green);
    flex: none;
  }
  .business-name {
    margin: 0;
    font-family: "Open Sans", Arial, sans-serif;
    font-weight: 400;
    font-size: 46px;
    line-height: 58px;
    color: var(--brand-blue);
  }
  .contact-block {
    color: var(--text-white);
  }
  .person-name {
    position: absolute;
    right: 35px;
    top: 48px;
    margin: 0;
    font-weight: 400;
    font-size: 31px;
    color: var(--brand-blue);
  }
  .person-title {
    position: absolute;
    right: 35px;
    top: 100px;
    margin: 0;
    font-size: 20px;
  }
  .contact-line {
    position: absolute;
    right: 76px;
    font-size: 22px;
    line-height: 30px;
    text-align: right;
    white-space: nowrap;
  }
  .contact-icon {
    position: absolute;
    left: 910px;
    width: 28px;
    height: 28px;
  }
  .phone { top: 311px; }
  .email { top: 351px; }
  .address { top: 407px; }
  .address-2 { top: 439px; }
  .abn {
    top: 485px;
    right: 43px;
    color: var(--brand-blue);
  }
  .icon-phone { top: 312px; }
  .icon-email { top: 352px; }
  .icon-home { top: 407px; }
</style>
</head>
<body>
  <div class="card">
    <svg class="card-shapes" viewBox="0 0 810 462" preserveAspectRatio="none" aria-hidden="true">
      <defs>
        <linearGradient id="band-gradient" x1="0" y1="0.5" x2="1" y2="0.5">
          <stop offset="0" stop-color="var(--band-deep)"/>
          <stop offset="0.6" stop-color="var(--band-light)"/>
        </linearGradient>
      </defs>
      <polygon class="chevron-band" fill="url(#band-gradient)" points="487,0 537,0 419,228 541,462 491,462 369,228"/>
      <polygon class="dark-panel" fill="var(--card-black)" points="537,0 810,0 810,462 541,462 419,228"/>
    </svg>

    <div class="brand">
      <span class="brand-mark" aria-hidden="true"></span>
      <h1 class="business-name">Tarnwick<br>Joinery</h1>
    </div>

    <div class="contact-block">
      <h2 class="person-name">Marcus Pelbury</h2>
      <p class="person-title">Qualified Carpenter</p>

      <div class="contact-line phone">0419 586 274</div>
      <svg class="contact-icon icon-phone" viewBox="0 0 28 28" aria-hidden="true">
        <circle cx="14" cy="14" r="12" fill="none" stroke="#fff" stroke-width="2"/>
        <path d="M10 8 l3 0 l1 4 l-2 1.5 q1.5 3 4 4.5 l1.5 -2 l4 1 l0 3 q-1 1.5 -3 1 q-8 -2 -10 -10 q-0.5 -2 1.5 -3z" fill="#fff"/>
      </svg>

      <div class="contact-line email">marcpelbury@tarnmail.example</div>
      <svg class="contact-icon icon-email" viewBox="0 0 28 28" aria-hidden="true">
        <path d="M3 11 L14 4 L25 11 L25 24 L3 24 Z" fill="#fff"/>
        <path d="M3 12 L14 19 L25 12" fill="none" stroke="var(--card-black)" stroke-width="1.6"/>
        <rect x="8" y="8" width="12" height="7" fill="var(--card-black)"/>
        <rect x="9.5" y="10" width="9" height="1.2" fill="#fff"/>
        <rect x="9.5" y="12.5" width="9" height="1.2" fill="#fff"/>
      </svg>

      <div class="contact-line address">PO Box 617 KELVALE</div>
      <div class="contact-line address-2">VIC 3918</div>
      <svg class="contact-icon icon-home" viewBox="0 0 28 28" aria-hidden="true">
        <path d="M14 3 L26 14 L22.5 14 L22.5 25 L16.5 25 L16.5 18 L11.5 18 L11.5 25 L5.5 25 L5.5 14 L2 14 Z" fill="#fff"/>
      </svg>

      <div class="contact-line abn">ABN:47 608 924 315</div>
    </div>
  </div>
</body>
</html>
```